Letterhead & Business Card Design Project

Use existing logo to create a new letterhead and business card design. Looking for something clean modern using color options of black, white and gray. The green from the logo may be used lightly as an accent color.

Target Market(s)

Professional business people

Industry/Entity Type

Business

Requirements
Must have
• Business card with front and back design using existing logo.
Nice to have
• Professional presentation
Clean look
Should not have
• No oil rigs, pumpjacks or clip art.

```html
<!DOCTYPE html>
<html lang="en">
<head>
<meta charset="utf-8">
<title>Ridgeline Resources – Business Card</title>
<link rel="stylesheet" href="https://fonts.googleapis.com/css2?family=Cinzel:wght@400&family=Montserrat:wght@300;400&display=swap">
<style>
  :root {
    --backdrop: #3b3b3b;
    --card-white: #ffffff;
    --band-gray: #8c8c8c;
    --back-gray-light: #8e8e8e;
    --back-gray-dark: #6a6a6a;
    --ink-dark: #2a2a2a;
    --ink-mid: #5a5a5a;
    --ink-light: #ececec;
    --accent-green: #2bb52b;
  }
  * { box-sizing: border-box; margin: 0; padding: 0; }
  html, body {
    width: 1200px;
    height: 900px;
    overflow: hidden;
    background: var(--backdrop);
  }
  .sheet {
    width: 1200px;
    height: 900px;
    display: flex;
    flex-direction: column;
    align-items: center;
    justify-content: center;
    gap: 56px;
  }
  .card {
    width: 640px;
    height: 366px;
    position: relative;
    overflow: hidden;
    box-shadow: 0 10px 28px rgba(0, 0, 0, 0.45);
  }

  /* Back of card */
  .card--back {
    background: linear-gradient(160deg, var(--back-gray-light), var(--back-gray-dark));
    display: flex;
    flex-direction: column;
    align-items: center;
    justify-content: center;
  }
  .brand-name {
    font-family: "Cinzel", serif;
    font-weight: 400;
    color: var(--ink-dark);
    letter-spacing: 0.08em;
    line-height: 1;
  }
  .card--back .brand-name {
    font-size: 44px;
    margin-top: -20px;
  }
  .website {
    position: absolute;
    bottom: 42px;
    left: 0;
    right: 0;
    text-align: center;
    font-family: "Cinzel", serif;
    font-size: 13px;
    letter-spacing: 0.14em;
    color: var(--ink-light);
  }

  /* Front of card */
  .card--front {
    background: var(--card-white);
    font-family: "Montserrat", sans-serif;
  }
  .identity {
    position: absolute;
    top: 34px;
    left: 44px;
  }
  .person-name {
    font-size: 22px;
    font-weight: 400;
    color: var(--accent-green);
    letter-spacing: 0.01em;
  }
  .person-title {
    font-size: 13px;
    font-weight: 300;
    color: var(--ink-mid);
    margin-top: 3px;
  }
  .info-band {
    position: absolute;
    top: 108px;
    left: 0;
    width: 100%;
    height: 146px;
    background: var(--band-gray);
  }
  .address {
    position: absolute;
    top: 22px;
    left: 44px;
    font-style: normal;
    font-size: 14px;
    font-weight: 300;
    line-height: 1.45;
    color: var(--ink-light);
  }
  .card--front .brand-name {
    position: absolute;
    right: 40px;
    bottom: 30px;
    font-size: 30px;
  }
  .contact-lines {
    position: absolute;
    top: 276px;
    left: 44px;
    list-style: none;
    font-size: 14px;
    font-weight: 300;
    line-height: 1.45;
    color: var(--ink-mid);
  }
  .contact-label {
    color: var(--accent-green);
    font-weight: 400;
    margin-right: 5px;
  }
</style>
</head>
<body>
  <main class="sheet">
    <section class="card card--back" aria-label="Business card back">
      <p class="brand-name">Ridgeline Resources</p>
      <p class="website">www.RidgelineResources.com</p>
    </section>

    <section class="card card--front" aria-label="Business card front">
      <div class="identity">
        <p class="person-name">Daniel Harwick</p>
        <p class="person-title">Managing Director</p>
      </div>
      <div class="info-band">
        <address class="address">
          4420 North Elm Street<br>
          Suite 210<br>
          Lakewood, Colorado 80226
        </address>
        <p class="brand-name">Ridgeline Resources</p>
      </div>
      <ul class="contact-lines">
        <li><span class="contact-label">P</span>555.240.1193</li>
        <li><span class="contact-label">F</span>555.240.1194</li>
      </ul>
    </section>
  </main>
</body>
</html>
```